Venture Capital Investment Firm

We are looking to overhaul our existing website (substantially), with only using the same logos (which we can provide).
We are an investment firm that focuses on making loans to late stage technology companies. Our site should ultimately look like other venture capital firms, and look modern and fresh. We have an existing website www.northvaleloan.com which this will be replacing, although we will be using a lot of the existing written content, and potentially the numbers of pages we will need, we are not wed to anything else. Please feel free to shoot any questions at any time and thank you in advance for your help!
Websites we like as examples:
https://www.tkbrandel.com/
https://www.emberwoodfunds.com/
Target Market(s)
Potential investors who will invest in our firm, as well as potentially companies that are looking to borrow money from us.

```html
<!DOCTYPE html>
<html lang="en">
<head>
<meta charset="utf-8">
<title>Northvale Loan — Private Investment Firm</title>
<link href="https://fonts.googleapis.com/css2?family=Playfair+Display:wght@600;700&family=Poppins:wght@400;500;600&display=swap" rel="stylesheet">
<style>
:root{
  --navy:#15164d;
  --navy-deep:#0e0f3c;
  --navy-stripe:#22246a;
  --ink:#1b1b2b;
  --muted:#5d5f70;
  --line:#e4e4ec;
  --white:#ffffff;
  --card:#f4f4f7;
  --map:#e6e7ea;
}
*{box-sizing:border-box;margin:0;padding:0}
html,body{width:1200px;height:3632px;overflow:hidden}
body{position:relative;background:var(--white);font-family:"Poppins",sans-serif;color:var(--ink)}
.serif{font-family:"Playfair Display",serif}
.abs{position:absolute}
.btn{display:inline-block;background:var(--navy);color:var(--white);font-size:15px;font-weight:600;padding:12px 26px;border-radius:4px}
.btn.light{background:var(--white);color:var(--navy)}
.label{font-size:16px;font-weight:600}

/* hero */
.hero{left:0;top:0;width:1200px;height:560px;overflow:hidden}
.hero-photo{position:absolute;inset:0;background:linear-gradient(120deg,#6f7480 0%,#a9adb6 35%,#d8d9dd 60%,#8e929c 100%)}
.hero-shade{position:absolute;inset:0;background:rgba(20,22,60,.25)}
.nav{position:absolute;left:0;top:0;width:1200px;height:100px;display:flex;align-items:center;padding:0 96px}
.brand{display:flex;align-items:center;gap:12px;color:var(--white);font-family:"Playfair Display",serif;font-size:26px;font-weight:700}
.brand-dot{width:34px;height:34px;border-radius:50%;background:var(--white)}
.nav-links{display:flex;gap:40px;margin-left:auto;margin-right:44px;color:var(--white);font-size:15px;font-weight:500}
.nav .btn{font-size:13px;padding:10px 18px}
.hero h1{position:absolute;left:0;width:1200px;top:222px;text-align:center;color:var(--white);font-size:60px;line-height:66px;font-weight:700}
.hero-arrow{position:absolute;left:1064px;top:272px;width:42px;height:42px;border-radius:50%;background:var(--white)}

/* about */
.about-text{left:96px;top:656px;width:460px}
.about-text h2{font-size:38px;line-height:46px;margin:10px 0 12px;color:var(--navy);white-space:nowrap}
.about-text .lead{font-size:16px;margin-bottom:10px}
.about-text p{font-size:14px;line-height:22px;color:var(--muted)}
.about-text .btn{margin-top:40px}
.about-photo{left:568px;top:620px;width:540px;height:390px;border-radius:10px;background:radial-gradient(circle at 50% 35%,#f3c86a 0%,#9b6c2a 30%,#2f3a1c 65%,#1a2212 100%)}

/* strategy band */
.band{left:0;top:1140px;width:1200px;height:560px;background:var(--navy-deep);overflow:hidden}
.stripe{position:absolute;background:var(--navy-stripe);transform:skewX(-35deg)}
.focus{position:absolute;width:240px;color:var(--white);text-align:center}
.focus-icon{width:80px;height:90px;margin:0 auto;border-radius:10px;background:var(--navy-stripe);display:flex;align-items:center;justify-content:center;box-shadow:0 0 0 3px #3b3fa0}
.focus h3{font-size:19px;margin:36px 0 10px}
.focus p{font-size:12px;line-height:18px;color:#c9cae0}
.circle-arrow{width:30px;height:30px;border-radius:50%;background:var(--white);margin:20px auto 0;display:flex;align-items:center;justify-content:center}
.strategy{left:680px;top:1296px;width:420px;color:var(--white)}
.strategy h2{font-size:44px;line-height:52px;margin:6px 0 12px}
.strategy .lead{font-size:15px;font-weight:600;margin-bottom:10px}
.strategy p{font-size:13px;line-height:20px;color:#c9cae0}
.strategy .btn{margin-top:28px}

/* team */
.team-head{left:0;width:1200px;top:1740px;text-align:center}
.team-head h2{font-size:48px;color:var(--ink);margin-top:2px}
.member{position:absolute;top:1832px;width:304px;height:456px;background:var(--card);border-radius:10px;overflow:hidden;text-align:center}
.member-photo{height:200px;background:linear-gradient(180deg,#8a8a8a 0%,#4c4c4c 100%)}
.member h3{font-size:20px;margin-top:32px}
.member .role{font-size:11px;color:var(--muted);margin-top:2px}
.member .area{font-size:15px;font-weight:600;margin-top:10px}
.member p{font-size:12px;line-height:18px;color:var(--muted);padding:6px 34px 0}
.socials{display:flex;justify-content:center;gap:8px;margin-top:18px}
.socials span{width:26px;height:26px;border-radius:50%;background:var(--navy)}

/* news */
.news{left:0;top:2360px;width:1200px;height:580px;background:var(--navy-deep);overflow:hidden}
.news-head{left:96px;top:2416px;color:var(--white)}
.news-head h2{font-size:64px;margin-top:14px;font-weight:700}
.post{position:absolute;top:2472px;width:190px}
.post-photo{height:162px}
.post-body{background:var(--white);padding:12px 14px 16px;height:176px}
.post-body .date{font-size:11px;font-weight:600}
.post-body h3{font-size:18px;margin:4px 0 4px}
.post-body p{font-size:10px;line-height:14px;color:var(--muted)}
.post-body .more{display:flex;align-items:center;gap:8px;font-size:11px;font-weight:600;margin-top:10px}
.post-body .more i{width:20px;height:20px;border-radius:50%;background:var(--navy);display:inline-block}

/* office */
.map{left:0;top:2940px;width:1200px;height:400px;background:linear-gradient(135deg,#eceef0,#d9dbdf 50%,#e8e9ec)}
.office-card{left:88px;top:2980px;width:264px;height:282px;background:var(--navy);color:var(--white);padding:28px 26px}
.office-card h2{font-size:32px;margin-bottom:16px}
.office-card .addr{display:flex;gap:10px;font-size:13px;line-height:20px}
.office-card .follow{font-size:14px;font-weight:600;margin-top:22px}
.office-card .socials{justify-content:flex-start;margin-top:10px}
.office-card .socials span{background:var(--white);width:30px;height:30px}

/* footer */
.footer{left:96px;top:3376px;width:1008px;display:flex;font-size:12px}
.footer h4{font-family:"Playfair Display",serif;font-size:20px;margin-bottom:14px}
.footer .col-contact{width:516px;display:grid;grid-template-columns:190px 190px;row-gap:14px}
.footer .col-contact h4{grid-column:1/3;margin-bottom:0}
.footer .col-contact b{display:block;font-weight:600}
.footer .col-contact span{color:var(--muted)}
.footer .col-links{width:360px}
.footer .col-links ul{list-style:none;display:grid;grid-template-columns:120px 120px;row-gap:8px;color:var(--muted)}
.footer .col-office .addr{display:flex;gap:8px;color:var(--muted);line-height:18px}
.footer .col-office .socials{justify-content:flex-start;margin-top:16px}
.footer .col-office .socials span{width:30px;height:30px}
.copyright{left:0;top:3596px;width:1200px;height:36px;border-top:1px solid var(--line);text-align:center;font-size:11px;color:var(--muted);line-height:36px}
</style>
</head>
<body>

<section class="hero abs">
  <div class="hero-photo" role="img" aria-label="Close-up of a businessman's hands reviewing financial documents with a pen at a desk"></div>
  <div class="hero-shade"></div>
  <svg class="abs" style="left:0;top:0" width="1200" height="560" viewBox="0 0 1200 560"><polygon points="0,420 0,560 1200,560 1200,500 520,560" fill="#fff"/><polygon points="0,300 0,560 400,560" fill="#fff"/></svg>
  <nav class="nav">
    <div class="brand"><span class="brand-dot"></span>Northvale Loan</div>
    <div class="nav-links"><span>Home</span><span>Strategy</span><span>About us</span><span>Team</span><span>News</span><span>Contact</span></div>
    <span class="btn">Newsletter</span>
  </nav>
  <h1 class="serif">Northvale Loan is a<br>Private Investment Firm</h1>
  <div class="hero-arrow"><svg width="42" height="42" viewBox="0 0 42 42"><path d="M18 14l7 7-7 7" stroke="#15164d" stroke-width="2.5" fill="none"/></svg></div>
</section>

<section class="about-text abs">
  <div class="label">About us</div>
  <h2 class="serif">Northvale Loan Started<br>With A Big Idea</h2>
  <div class="lead">Finance proven innovation with a different approach</div>
  <p>Northvale Loan is a private investment firm created to back the science and technology companies behind lasting change. Our team brings deep experience in intellectual property, credit and growth strategy to every partnership we build.</p>
  <span class="btn">Read More</span>
</section>
<div class="about-photo abs" role="img" aria-label="Glowing light bulb resting on soil beside a young green sprout"></div>

<section class="band abs">
  <div class="stripe" style="left:760px;top:0;width:160px;height:560px"></div>
  <div class="stripe" style="left:1000px;top:0;width:110px;height:560px"></div>
  <div class="stripe" style="left:-120px;top:0;width:180px;height:560px;opacity:.6"></div>
</section>
<div class="focus" style="left:88px;top:1288px">
  <div class="focus-icon"><svg width="40" height="40" viewBox="0 0 40 40"><rect x="6" y="14" width="28" height="20" fill="none" stroke="#fff" stroke-width="2"/><path d="M14 14V8h12v6" fill="none" stroke="#fff" stroke-width="2"/></svg></div>
  <h3 class="serif">Industry Focus</h3>
  <p>Our focus spans the life science and technology industries, backing teams whose patents form an integral driver of value.</p>
  <div class="circle-arrow"><svg width="12" height="12" viewBox="0 0 12 12"><path d="M2 6h8M7 3l3 3-3 3" stroke="#15164d" stroke-width="1.6" fill="none"/></svg></div>
</div>
<div class="focus" style="left:400px;top:1288px">
  <div class="focus-icon"><svg width="40" height="40" viewBox="0 0 40 40"><rect x="8" y="6" width="24" height="28" fill="none" stroke="#fff" stroke-width="2"/><path d="M13 14h14M13 20h14M13 26h9" stroke="#fff" stroke-width="2"/></svg></div>
  <h3 class="serif">Transaction Types</h3>
  <p>Northvale Loan offers flexible structures built around identifying growth opportunities in mature enterprise assets.</p>
  <div class="circle-arrow"><svg width="12" height="12" viewBox="0 0 12 12"><path d="M2 6h8M7 3l3 3-3 3" stroke="#15164d" stroke-width="1.6" fill="none"/></svg></div>
</div>
<div class="strategy abs">
  <div class="label">Strategy</div>
  <h2 class="serif">Partners For Growth</h2>
  <div class="lead">We provide flexible capital to innovative companies and their investors</div>
  <p>Our focus spans the life science and technology industries, backing teams whose intellectual property is an integral driver of value.</p>
  <span class="btn light">Read More</span>
</div>

<section class="team-head abs">
  <div class="label">Team</div>
  <h2 class="serif">Meet Our Team</h2>
</section>
<article class="member" style="left:104px">
  <div class="member-photo" role="img" aria-label="Black and white portrait of Milo Hartwell"></div>
  <h3 class="serif">Milo Hartwell</h3>
  <div class="role">Managing Partner</div>
  <div class="area">Life Science, Technology</div>
  <p>Milo has spent two decades investing in science-led businesses and leads the firm's origination, underwriting and portfolio management.</p>
  <div class="socials"><span></span><span></span></div>
</article>
<article class="member" style="left:448px">
  <div class="member-photo" role="img" aria-label="Black and white portrait of Dev Ranganathan"></div>
  <h3 class="serif">Dev Ranganathan</h3>
  <div class="role">Managing Partner</div>
  <div class="area">Technology</div>
  <p>Dev leads technology investments, bringing fifteen years of experience across growth lending and enterprise software.</p>
  <div class="socials"><span></span><span></span></div>
</article>
<article class="member" style="left:792px">
  <div class="member-photo" role="img" aria-label="Black and white portrait of Owen Calder"></div>
  <h3 class="serif">Owen Calder</h3>
  <div class="role">Partner</div>
  <div class="area">Chief Operating Officer</div>
  <p>Owen oversees operations and reporting, with long experience in alternative investment markets and fund administration.</p>
  <div class="socials"><span></span><span></span></div>
</article>

<section class="news abs">
  <div class="stripe" style="left:-80px;top:0;width:200px;height:580px"></div>
  <div class="stripe" style="left:230px;top:0;width:120px;height:580px;opacity:.7"></div>
</section>
<div class="news-head abs">
  <div class="label">News</div>
  <h2 class="serif">Recent News</h2>
</div>
<article class="post" style="left:492px">
  <div class="post-photo" role="img" aria-label="Business team gathered around a table in a meeting" style="background:linear-gradient(135deg,#c9c3b8,#7c776f)"></div>
  <div class="post-body"><div class="date">April 2018</div><h3 class="serif">Recent News</h3><p>Northvale Loan completes structured debt investment in a growth-stage software company.</p><div class="more"><i></i>Find Out More</div></div>
</article>
<article class="post" style="left:700px">
  <div class="post-photo" role="img" aria-label="Rising stacks of coins with small green plants" style="background:linear-gradient(135deg,#d8e0b8,#6f8a3e)"></div>
  <div class="post-body"><div class="date">April 2018</div><h3 class="serif">Portfolio News</h3><p>Portfolio company closes a new funding round to expand its platform worldwide.</p><div class="more"><i></i>Find Out More</div></div>
</article>
<article class="post" style="left:908px">
  <div class="post-photo" role="img" aria-label="Hand holding a glowing light bulb against a dark background" style="background:radial-gradient(circle at 50% 40%,#f0c060,#3a2a16 60%,#120e0a)"></div>
  <div class="post-body"><div class="date">July 2018</div><h3 class="serif">Press Release</h3><p>Northvale Loan welcomes a new partner to lead technology investment strategy.</p><div class="more"><i></i>Find Out More</div></div>
</article>

<section class="map abs" role="img" aria-label="Street map of the San Francisco neighborhood around the office"></section>
<svg class="abs" style="left:434px;top:3052px" width="30" height="40" viewBox="0 0 30 40"><path d="M15 1C7 1 1 7 1 15c0 10 14 24 14 24s14-14 14-24C29 7 23 1 15 1z" fill="#d43b3b"/><circle cx="15" cy="15" r="5" fill="#fff"/></svg>
<div class="office-card abs">
  <h2 class="serif">Our Office</h2>
  <div class="addr"><svg width="14" height="18" viewBox="0 0 14 18"><path d="M7 1C3.7 1 1 3.7 1 7c0 5 6 10 6 10s6-5 6-10c0-3.3-2.7-6-6-6z" fill="#fff"/></svg><div>San Francisco<br>2218 Larkmont Street #310<br>San Francisco, CA 94107</div></div>
  <div class="follow">Follow Us</div>
  <div class="socials"><span></span><span></span><span></span><span></span></div>
</div>

<footer class="footer abs">
  <div class="col-contact">
    <h4>Contact Us</h4>
    <div><b>General inquiries</b><span>info@northvaleloan.com</span></div>
    <div><b>Media inquiries</b><span>media@northvaleloan.com</span></div>
    <div><b>Transaction opportunities</b><span>deals@northvaleloan.com</span></div>
    <div><b>Careers</b><span>careers@northvaleloan.com</span></div>
  </div>
  <div class="col-links">
    <h4>Quick Links</h4>
    <ul><li>Home</li><li>News</li><li>Strategy</li><li>Contact</li><li>About us</li><li>Investors</li><li>Team</li></ul>
  </div>
  <div class="col-office">
    <h4>Our Office</h4>
    <div class="addr"><svg width="12" height="16" viewBox="0 0 14 18"><path d="M7 1C3.7 1 1 3.7 1 7c0 5 6 10 6 10s6-5 6-10c0-3.3-2.7-6-6-6z" fill="#15164d"/></svg><div>San Francisco<br>2218 Larkmont Street #310<br>San Francisco, CA 94107</div></div>
    <div class="socials"><span></span><span></span><span></span><span></span></div>
  </div>
</footer>
<div class="copyright abs">© 2018 Northvale Loan Investment Partners. All Rights Reserved.</div>

</body>
</html>
```